"Maple Nook" needs a A5 flyer for its "Art Contest"

Maple Nook needs a double sided A5 Flyer that illustrates in a child-friendly look the following competition:

Search for the up and coming Bright Sprout. The aim of our Bright Sprout is to allow our children to explore the artist within them and motivate them to express their talents through the fine art of drawing and painting.

Description: I have an art school, "Maple Nook", where children of 3-5 years old attend and learn how to paint and draw. We are making a competition where each child gets to draw a picture which we will upload to Chirpwall and parents will vote for best picture. We need to distribute to the parents a flyer with following content.

Competition Name: Bright Sprout

Front Side (content):
No major text on the front. Only the Logo and messages grabbing the readers attention such as "Who will be our next Artist?", "Vote for your Child", "Like Us on our Chirpwall Page".

Back Side (content):
Back side content is divided into 3 sections:

Section1:
How it Works?
Every child of every class will participate. Photos will be grouped by class.
There will be a Bright Sprout for each class, and there will be a Bright Sprout for the school.

Section2:
How to Participate?
In our search for ‘Bright Sprout’, we will select one piece of artwork from each child in the school, photograph it and upload it to our Chirpwall page.
Vote for your favourite painting by following the steps below:
1- From your chirpwall account go to www.chirpwall.example/Maple Nook
and “Like Us” to become a fan
2- Click on the“Bright Sprout” from the application menu
3- Browse through the different classes and vote for each picture you like
4- Invite your friends to vote for the picture you like to increase the chances of winning
The artist of the painting with most “Likes” will be crowned ‘Bright Sprout’.

Section3:
Note (in the footer):
Please note that the winner’s photo will be displayed in our “Bright Sprout” Frame on our Chirpwall landing page. If you do not want your child’s photograph to be posted on our Chirpwall page in this manner, please let us know by sending an e-mail.
, Maple Nook needs a double sided A5 Flyer that illustrates in a child-friendly look the following competition:

Front Side (content):

Back Side (content):

Section1:
How it Works?

Section2:
How to Participate?

Section3:
Note (in the footer):

Reason: To give more time for improvements on submitted designs and if possible some additional submissions.

Target Market(s)

Parents of the children attending at our school, Parents of the children attending at our school

Industry/Entity Type

Painting

Requirements
Must have
• Colors used in the design should be strict to our logo colors. We have 4 colors in our logo feel free to use one or all of them through out the design:
#6CB53C
#DB2718
#5D9DD5
#F4D602

The elements in our logo are playful and hand drawn and written, so the flyer design should reflect the hand made style rather than solid elements and objects., Colors used in the design should be strict to our logo colors. We have 4 colors in our logo feel free to use one or all of them through out the design:
#6CB53C
#DB2718
#5D9DD5
#F4D602

The elements in our logo are playful and hand drawn and written, so the flyer design should reflect the hand made style rather than solid elements and objects.
Should not have
• Images of real children., Images of real children.

```html
<!DOCTYPE html>
<html lang="en">
<head>
<meta charset="utf-8">
<title>Maple Nook – Bright Sprout Flyer</title>
<link rel="stylesheet" href="https://fonts.googleapis.com/css2?family=Chewy&family=Comic+Neue:wght@400;700&display=swap">
<style>
  :root {
    --green: #6CB53C;
    --red: #DB2718;
    --blue: #5D9DD5;
    --yellow: #F4D602;
    --orange: #EE7A1E;
    --teal: #4FA7A0;
    --ink: #3a3a3a;
    --paper: #ffffff;
    --wash-blue: #cfe3ee;
    --wash-yellow: #f7efb3;
    --wash-pink: #f3c6bf;
    --wash-green: #d8ebc0;
  }
  * { margin: 0; padding: 0; box-sizing: border-box; }
  html, body { width: 1200px; height: 782px; overflow: hidden; background: var(--paper); }
  body { position: relative; font-family: "Comic Neue", "Comic Sans MS", cursive; }

  .flyer-side { position: absolute; top: 0; height: 782px; overflow: hidden; }
  .flyer-front { left: 0; width: 551px; }
  .flyer-back { left: 649px; width: 551px; }

  .wash { position: absolute; inset: 0; }
  .flyer-front .wash {
    background:
      radial-gradient(circle at 20% 15%, var(--wash-blue) 0, transparent 45%),
      radial-gradient(circle at 80% 75%, var(--wash-pink) 0, transparent 45%),
      radial-gradient(circle at 30% 85%, var(--wash-yellow) 0, transparent 50%),
      radial-gradient(circle at 75% 30%, var(--wash-green) 0, transparent 45%),
      linear-gradient(160deg, #dfeadf, #f6efc4 55%, #f1d9c6);
  }
  .flyer-back .wash {
    background:
      radial-gradient(circle at 55% 50%, var(--wash-blue) 0, transparent 35%),
      radial-gradient(circle at 20% 40%, var(--wash-yellow) 0, transparent 40%),
      radial-gradient(circle at 85% 55%, var(--wash-pink) 0, transparent 35%),
      radial-gradient(circle at 40% 90%, var(--wash-yellow) 0, transparent 45%),
      linear-gradient(170deg, #d6e6ef, #f3edc4 55%, #f2dcc8);
  }

  .brand {
    position: absolute; left: 12px; top: 12px;
    display: flex; align-items: center; gap: 5px;
    font-weight: 700; font-size: 15px; color: var(--green);
  }
  .brand-mark { width: 11px; height: 11px; border-radius: 50%; background: var(--green); }

  .crayon-art {
    position: absolute; left: 321px; top: 65px; width: 230px; height: 195px;
    background: radial-gradient(ellipse at 50% 50%, rgba(93,157,213,.25), rgba(244,214,2,.18) 50%, transparent 72%);
  }

  .headline { position: absolute; inset: 0; font-weight: 400; }
  .headline span {
    position: absolute; font-family: "Chewy", "Comic Neue", cursive; line-height: 1;
    -webkit-background-clip: text; background-clip: text; color: transparent;
    white-space: nowrap;
  }
  .hl-who    { left: 184px; top: 184px; font-size: 86px;
               transform: translate(-50%, -50%) rotate(35deg);
               background-image: linear-gradient(90deg, var(--yellow), var(--green) 60%, var(--teal)); }
  .hl-will   { left: 196px; top: 300px; font-size: 80px;
               transform: translate(-50%, -50%) rotate(-18deg);
               background-image: linear-gradient(90deg, var(--yellow), var(--green)); }
  .hl-next   { left: 335px; top: 382px; font-size: 82px;
               transform: translate(-50%, -50%) rotate(-30deg);
               background-image: linear-gradient(90deg, var(--orange), var(--yellow) 35%, var(--green) 65%, var(--teal)); }
  .hl-artist { left: 282px; top: 500px; font-size: 92px;
               transform: translate(-50%, -50%) rotate(-30deg);
               background-image: linear-gradient(90deg, var(--red), var(--orange) 30%, var(--green) 65%, var(--teal)); }

  .tagline { position: absolute; font-size: 19px; white-space: nowrap; transform: translate(-50%, -50%); }
  .tag-vote { left: 131px; top: 684px; color: var(--blue); transform: translate(-50%, -50%) rotate(8deg); }
  .tag-like { left: 391px; top: 728px; color: var(--green); transform: translate(-50%, -50%) rotate(-8deg); }

  .back-copy {
    position: absolute; left: 30px; top: 60px; right: 12px;
    color: var(--ink); font-size: 15px; line-height: 20px; white-space: nowrap;
  }
  .section-participate { margin-top: 142px; }
  .indent { padding-left: 18px; display: block; }

  .footer-note {
    position: absolute; left: 8px; top: 700px; right: 4px;
    color: var(--ink); font-size: 10.5px; line-height: 11.5px; white-space: nowrap;
  }
</style>
</head>
<body>
  <section class="flyer-side flyer-front">
    <div class="wash" role="img" aria-label="Soft pastel mosaic background in blue, yellow, green and pink"></div>
    <div class="brand"><span class="brand-mark"></span>Maple Nook</div>
    <div class="crayon-art" role="img" aria-label="Hand-drawn crayon pencil in red, yellow, green and blue"></div>
    <h1 class="headline" aria-label="Who will be our next Artist?">
      <span class="hl-who">Who</span>
      <span class="hl-will">will be</span>
      <span class="hl-next">our next</span>
      <span class="hl-artist">Artist?</span>
    </h1>
    <p class="tagline tag-vote">vote for your children</p>
    <p class="tagline tag-like">Like us on our chirpwall page</p>
  </section>

  <section class="flyer-side flyer-back">
    <div class="wash" role="img" aria-label="Soft pastel mosaic background in a swirl of blue, yellow and pink"></div>
    <div class="back-copy">
      <div class="section-how">
        <p>How it Works?</p>
        <p>Every child of every class will participate.</p>
        <p>Photos will be grouped by class.</p>
        <p>There will be a Bright Sprout for each class,</p>
        <p>and there will be a Bright Sprout for the school.</p>
      </div>
      <div class="section-participate">
        <p>How to Participate?</p>
        <p>In our search for ‘Bright Sprout’,</p>
        <p>we will select one piece of artwork from each child in the school,</p>
        <p>photograph it and upload it to our Chirpwall page.</p>
        <p>Vote for your favourite painting by following the steps below:</p>
        <p>1- From your chirpwall account<span class="indent">go to www.chirpwall.example/Maple Nook</span><span class="indent">and “Like Us” to become a fan</span></p>
        <p>2- Click on the“Bright Sprout” from the application menu</p>
        <p>3- Browse through the different classes<span class="indent">and vote for each picture you like</span></p>
        <p>4- Invite your friends to vote for the picture you like<span class="indent">to increase the chances of winning</span><span class="indent">The artist of the painting with most “Likes”</span><span class="indent">will be crowned ‘Bright Sprout’.</span></p>
      </div>
    </div>
    <footer class="footer-note">
      <p>Note</p>
      <p>Please note that the winner’s photo will be displayed</p>
      <p>in our “Bright Sprout” Frame on our Chirpwall landing page.</p>
      <p>If you do not want your child’s photograph to be posted on our Chirpwall page in this manner,</p>
      <p>please let us know by sending an e-mail.</p>
    </footer>
  </section>
</body>
</html>
```